Healthy Food Healthy Brain Rack Card

We want a new 2 page (front and page) 3.67" x 8.5" rack card. This rack card is the first of a series we are creating. We will have five more eventually.

The minimum font size for the text on the front is 11 point and also for other main body text.

Use the text on the word document.

The images and layout in the word document are just sample ideas we had.

We have a subscripton to adobe stock images so prefer to get images from there or free high quality images.

The document is for older readers. Do not put text over graphics and keep it simple and easy to read with high contrast.

We are open to any color scheme, though something that conveys fresh and healthy, is good.

We want some very simple design element(s) incorporated that convey Native American communities or heritage. But NO head dress, teepee graphics, etc.

At the top, of the first page we would like a collage of healthy food images. This can include fish, chicken, fresh vegetables, berries, brown rice, etc.

On the back side, the text below the brown box on the word document with the title "mock up" can be smaller as needed.

Please remember to include the funding statement - it can be in a very small font 6/7 point.

For more information about our project, please visit https://velmorcollective.org/mind-care/

```html
<!DOCTYPE html>
<html lang="en">
<head>
<meta charset="utf-8">
<title>Healthy Food, Healthy Brain – Rack Card</title>
<link href="https://fonts.googleapis.com/css2?family=Oswald:wght@600;700&family=Poppins:ital,wght@0,400;0,600;0,700;1,400&display=swap" rel="stylesheet">
<style>
  :root{
    --teal:#4aa6ad;
    --rust:#b05f55;
    --ink:#1d1d1d;
    --paper:#ffffff;
    --backdrop:#e7ecec;
  }
  *{box-sizing:border-box;margin:0;padding:0}
  html,body{width:1200px;height:1200px;overflow:hidden;background:var(--backdrop)}
  body{position:relative;font-family:"Poppins",sans-serif;color:var(--ink)}
  .card{position:absolute;top:107px;width:426px;height:986px;background:var(--paper);border:9px solid var(--teal);overflow:hidden}
  .card--front{left:150px;padding:22px 22px 0 22px}
  .card--back{left:624px;padding:18px 20px 0 19px}
  .display{font-family:"Oswald",sans-serif;font-weight:700;text-transform:uppercase;letter-spacing:-0.2px;white-space:nowrap}

  /* front */
  .front-title{color:var(--teal);font-size:29px;line-height:27px;text-align:center;width:430px;margin-left:-33px;transform:scaleX(.84);transform-origin:center}
  .collage{display:grid;grid-template-columns:112px 112px 133px;grid-template-rows:112px 113px;width:357px;height:225px;margin:6px 0 0 3px}
  .collage div{width:100%;height:100%}
  .tile-salmon{background:linear-gradient(135deg,#f3efe9,#f0875a 55%,#e8dcd0)}
  .tile-rice{background:linear-gradient(160deg,#f2ece0,#e4d8bf 60%,#fafafa)}
  .tile-berries{grid-row:span 2;background:radial-gradient(circle at 55% 65%,#8ea4c2 0,#6f86a8 40%,transparent 62%),linear-gradient(160deg,#3d7a33,#c92a3d 45%,#f4f4f4 85%)}
  .tile-veg{background:linear-gradient(135deg,#7a5a3a,#c9452f 45%,#5f8a3a 75%,#d99a59)}
  .tile-fish{background:linear-gradient(150deg,#f4ead8,#e9c79a 50%,#c9683b)}
  .quote{font-size:17px;line-height:21.5px;text-align:center;margin-top:12px}
  .quote cite{font-style:normal;display:block}
  .quote cite em{font-style:italic}
  .section-title{color:var(--rust);font-size:33px;line-height:34px;margin-top:20px;padding-bottom:1px;border-bottom:2px solid var(--rust);width:424px;transform:scaleX(.86);transform-origin:left}
  .body-copy{font-size:17.6px;line-height:21.2px;text-align:justify;margin-top:4px}
  .steps-title{color:var(--teal);font-size:23px;line-height:26px;margin-top:20px;transform:scaleX(.86);transform-origin:left}
  .steps{list-style:none;margin-top:10px;padding-right:26px;position:relative}
  .steps::before{content:"";position:absolute;left:6px;top:8px;bottom:2px;width:1px;background:var(--teal)}
  .steps li{position:relative;padding-left:27px;font-size:17.4px;line-height:21.2px;margin-bottom:5px}
  .steps li::before{content:"";position:absolute;left:1px;top:5px;width:11px;height:11px;border-radius:50%;background:var(--teal)}

  /* back */
  .back-title{color:var(--teal);font-size:54px;line-height:52px;transform:scaleX(.84);transform-origin:left}
  .recipe-name{color:var(--rust);font-weight:700;font-size:18px;line-height:20px;padding-bottom:6px;border-bottom:1.5px solid var(--teal);white-space:nowrap}
  .recipe-top{display:flex;gap:16px;margin-top:12px}
  .recipe-photo{width:127px;height:156px;flex:none;background:linear-gradient(160deg,#f7f2ec,#f28a5b 40%,#ee7a48 70%,#f3ece4)}
  .ingredients h3{color:var(--rust);font-size:18.5px;line-height:20px;font-weight:700}
  .ingredients ul{list-style:none}
  .ingredients li{font-size:17px;line-height:21.3px;white-space:nowrap}
  .ingredients li.note{font-size:14px}
  .dot{display:inline-block;width:9px;height:9px;border-radius:50%;background:var(--rust);margin-right:5px;vertical-align:1px}
  .method{font-size:17px;line-height:19.3px;text-align:justify;margin-top:12px;letter-spacing:.2px}
  .callout{background:var(--rust);color:#fff;border-radius:7px;text-align:center;font-size:17.4px;line-height:19.4px;padding:11px 18px 10px;margin-top:8px}
  .more{text-align:center;margin-top:10px}
  .more-title{display:inline-block;color:var(--teal);font-weight:700;font-size:20px;line-height:24px;border-bottom:1.5px solid var(--teal);padding-bottom:1px}
  .more h4{color:var(--rust);font-weight:700;font-size:19px;line-height:22px;margin-top:9px}
  .more p{font-size:16.5px;line-height:18px}
  .more .url{font-family:Arial,sans-serif;font-size:16px}
  .more .url b{font-weight:700}
  .more .gap{margin-top:11px}
  .brand{display:flex;align-items:center;justify-content:center;gap:10px;margin-top:12px}
  .brand-circle{width:54px;height:54px;border-radius:50%;background:var(--teal);flex:none}
  .brand-name{color:var(--teal);font-weight:600;font-size:15px;line-height:17px;text-align:left}
  .funding{font-family:Arial,sans-serif;font-size:8px;line-height:11.5px;text-align:center;color:#333;margin-top:10px}
</style>
</head>
<body>

<section class="card card--front">
  <h1 class="display front-title">Talk to your doctor about more<br>steps to healthier food choices.</h1>
  <div class="collage">
    <div class="tile-salmon" role="img" aria-label="Photo of raw salmon steaks with lemon"></div>
    <div class="tile-rice" role="img" aria-label="Photo of a bowl of brown rice"></div>
    <div class="tile-berries" role="img" aria-label="Photo of blueberries, blackberries and raspberries"></div>
    <div class="tile-veg" role="img" aria-label="Photo of fresh vegetables"></div>
    <div class="tile-fish" role="img" aria-label="Photo of grilled white fish"></div>
  </div>
  <blockquote class="quote">
    <strong>“</strong>Without the elk, salmon, huckleberries, shellfish, &amp; cedar trees we are nobody…<strong>”</strong>
    <cite>Marla Tenwick (<em>Kelwater</em>)</cite>
  </blockquote>
  <h2 class="display section-title">Healthy food, healthy brain</h2>
  <p class="body-copy">Everyone slows down as they get older, both in body &amp; mind. Eating healthier food can help your overall health, includ-ing brain health. It may also reduce your risk for memory loss &amp; problems thinking.</p>
  <h3 class="display steps-title">Healthier steps to protect your brain:</h3>
  <ul class="steps">
    <li>Eat more vegetables, fruits, whole grains, &amp; lower-fat milk</li>
    <li>Use less salt &amp; added sugar</li>
    <li>Eat more fish, chicken, turkey, beans, &amp; nuts</li>
    <li>Cut down on bad fats (“saturated” &amp; trans), cholesterol, &amp; red meat</li>
    <li>Buy fresh, not packaged food when you can</li>
    <li>Limit how much alcohol you drink</li>
    <li>Learn your daily calorie needs for your body size</li>
    <li>Take care of your mental &amp; spiritual health to support your physical &amp; brain health</li>
  </ul>
</section>

<section class="card card--back">
  <h1 class="display back-title">Make this at home</h1>
  <p class="recipe-name">GRILLED SALMON &amp; VEGGIE FOIL PACKETS</p>
  <div class="recipe-top">
    <div class="recipe-photo" role="img" aria-label="Photo of raw salmon steaks"></div>
    <div class="ingredients">
      <h3>INGREDIENTS:</h3>
      <ul>
        <li><span class="dot"></span>Salmon <span class="dot"></span>Asparagus</li>
        <li><span class="dot"></span>Red or Green Peppers</li>
        <li class="note"><span class="dot"></span>(Or any seasonal vegetable)</li>
        <li><span class="dot"></span>Onion <span class="dot"></span>Lemon-sliced</li>
        <li><span class="dot"></span>Basil <span class="dot"></span>Olive Oil</li>
        <li><span class="dot"></span>Salt &amp; Pepper</li>
        <li><span class="dot"></span>Garlic Powder</li>
      </ul>
    </div>
  </div>
  <p class="method">Cut asparagus, peppers, &amp; onion into bite-size pieces. Cut salmon into 4-6 oz pieces. Tear tin foil large enough to wrap around salmon &amp; veggies (2 layers). Add veggies &amp; salmon to foil. Drizzle with olive oil, season with salt, pepper, basil, garlic &amp; top with a piece of sliced lemon. Wrap foil tightly around food. Grill at 400 degrees for about 20 minutes. Careful opening!</p>
  <div class="callout">Food &amp; drink are a source of strength &amp; connection to community. A return to traditional food pathways &amp; eating local, seasonal fresh foods make healthier eating easier.</div>
  <div class="more">
    <span class="more-title">FOR MORE INFORMATION</span>
    <h4>About Healthier Eating</h4>
    <p>FreshPlate Guide</p>
    <p class="url">www.<b>freshplateguide</b>.org</p>
    <h4>About Brain Health</h4>
    <p>Velmor Collective Center for<br>Brain Health</p>
    <p class="url">www.<b>velmorcollective</b>.org</p>
    <p class="gap">Riverstone Memory Program</p>
    <p class="url"><b>https://www.riverstonememory.org/aging</b></p>
  </div>
  <div class="brand">
    <span class="brand-circle"></span>
    <span class="brand-name">VELMOR COLLECTIVE<br>CENTER FOR BRAIN HEALTH</span>
  </div>
  <p class="funding">This product is supported by the National Office for Community Wellness (NOCW) of the Federal Bureau of Public Care (FBPC) as part of a financial assistance award totaling $348,711 with 100 percent funded by NOCW/FBPC. The contents are those of the author(s) and do not necessarily represent the official views of, nor an endorsement, by NOCW/FBPC, or the Government.</p>
</section>

</body>
</html>
```